Hardcore nerd needs to stand out in a sea of dull Defence business cards

Wombat Devices is a new Australian consulting engineering company that turns research and theory into practical systems. No evangelistic fluff, just mathematics and physics into electronic and optical circuits for consumer products, scientific research or Defence applications.

We already have a recognised logo (provided) which is often dark blue/black on a light background but we're open to other combinations. (Us engineers tend to have limited aesthetic imagination :)

Some of our recent products have included:
* Instrumentation for electrical testing,
* Radar jammers,
* GPS antenna design,
* Satellite tracking systems,
* High power lasers

We're open to both single and double-sided designs - happy to be convinced either way.

P.S. Another group is working on the web page, so - alas - our web site is currently of no use for images/ideas...

Target Market(s)

Engineering managers,
Scientists

Contact Information for Business Card

Dr Colin Marsh
R&D Engineer

colin@wombatdevicesco.com.au
0427 563 210

PO Box XXX (to be confirmed)
Banks ACT 2913
Australia

Font styles to use
Serif
Sans Serif

Colors

Designer to choose colors to be used in the design.

Requirements
Must have
• My contact details!
• I've had many (great) "bold and plain" designs submitted already, so feel free to be artistically creative :)
• Happy to take advice re fonts/colours/printability etc.
Nice to have
• I'm not sure if "lists" are more at home on a CV than a business card, but representative services include:
• Applied electromagnetics
• RF and high speed electronics
• Signal and image processing
• Electro-optical and laser systems
• Concept-to-prototype design services
• If you're considering double sided cards, then often measuring/alignment grids/rulers feature on the back of similar cards.
• e.g. https://www.lumoptix-example.com/newgrouppage9.cfm?objectgroup_id=4815
• https://www.lumoptix-example.com/newgrouppage9.cfm?objectgroup_ID=4817
• ..or even a "Smith chart" (google will return lots)
• Generic images to represent a capability might work - googling images associated with keyword for each of these areas might help:
• - "passive radar", "phased array", "fdtd", "vircator"
• RF and high speed electronic design
• - "smith chart", "microstrip circuits", "dimensioned drawing", "electronic schematic"
• - "dft", "iir filter"
• - "optical cavity". "laser energy level diagram"
• Background/watermarked images outlines/wireframes/schematics would probably look OK.
Should not have
• If a list of projects/services is provided, it is important not to make the client feel that this is "all" the company can do. Engineering design is a creative discipline (like graphics :)
• Please, no stock "military" snaps like planes, missiles, etc!

```html
<!DOCTYPE html>
<html lang="en">
<head>
<meta charset="utf-8">
<title>Wombat Devices – Business Card</title>
<link rel="stylesheet" href="https://fonts.googleapis.com/css2?family=Lato:wght@400;700;900&family=Arimo:wght@700&display=swap">
<style>
  :root {
    --navy: #0b1f63;
    --navy-deep: #0a1f5e;
    --paper: #ffffff;
    --ink: #1d1d1d;
    --rule: #9a9a9a;
    --backdrop: #2b2b2b;
  }
  * { margin: 0; padding: 0; box-sizing: border-box; }
  html, body { width: 1200px; height: 1200px; overflow: hidden; }
  body {
    position: relative;
    background: var(--backdrop);
    font-family: "Lato", sans-serif;
  }
  .card {
    position: absolute;
    top: 310px;
    height: 594px;
    box-shadow: 0 6px 14px rgba(0,0,0,.55);
  }
  .card--front { left: 234px; width: 364px; background: var(--paper); color: var(--ink); }
  .card--back  { left: 628px; width: 368px; background: var(--navy-deep); color: var(--paper); }

  /* Front: wordmark */
  .brand {
    position: absolute;
    top: 118px;
    left: 42px;
    display: flex;
    align-items: center;
    gap: 12px;
    color: var(--navy);
  }
  .brand__dot {
    width: 62px; height: 62px;
    border-radius: 50%;
    background: var(--navy);
    flex: none;
  }
  .brand__name {
    font-weight: 900;
    line-height: 1;
  }
  .brand__name span { display: block; }
  .brand__line1 { font-size: 27px; letter-spacing: 1px; }
  .brand__line2 { font-size: 16px; letter-spacing: 3.4px; margin-top: 6px; }

  /* Front: person & contacts */
  .person {
    position: absolute;
    top: 337px; left: 0; right: 0;
    text-align: center;
  }
  .person__name {
    font-family: "Arimo", sans-serif;
    font-weight: 700;
    font-size: 21px;
    color: var(--navy);
    line-height: 26px;
  }
  .person__role { font-size: 16px; line-height: 20px; }

  .contact-icons {
    position: absolute;
    top: 396px; left: 87px;
    width: 190px; height: 24px;
    display: flex; align-items: center; justify-content: center; gap: 3px;
  }
  .contact-icons::before, .contact-icons::after {
    content: ""; flex: 1; height: 1px; background: var(--rule);
  }
  .contact-icons::before { margin-right: 2px; }
  .contact-icons::after { margin-left: 2px; }
  .contact-icons svg { width: 24px; height: 24px; flex: none; }

  .contacts {
    position: absolute;
    top: 426px; left: 0; right: 0;
    text-align: center;
    font-size: 16.5px;
    line-height: 22px;
  }
  .divider {
    position: absolute;
    top: 507px; left: 88px;
    width: 195px; height: 1px;
    background: var(--rule);
  }
  .address {
    position: absolute;
    top: 517px; left: 0; right: 0;
    text-align: center;
    font-size: 16.5px;
    line-height: 22px;
  }

  /* Back */
  .back-mark {
    position: absolute;
    top: 150px; left: 0; right: 0;
    display: flex; flex-direction: column; align-items: center; gap: 18px;
    color: var(--paper);
  }
  .back-mark__dot {
    width: 110px; height: 110px;
    border-radius: 50%;
    background: var(--paper);
  }
  .back-mark__name {
    font-weight: 900;
    font-size: 30px;
    letter-spacing: 2px;
    text-align: center;
    line-height: 1.15;
  }
  .services {
    position: absolute;
    top: 440px; left: 0; right: 0;
    list-style: none;
    text-align: center;
    font-size: 18px;
    line-height: 27px;
  }
</style>
</head>
<body>
  <section class="card card--front" aria-label="Business card front">
    <div class="brand">
      <div class="brand__dot"></div>
      <div class="brand__name">
        <span class="brand__line1">WOMBAT</span>
        <span class="brand__line2">DEVICES</span>
      </div>
    </div>

    <div class="person">
      <p class="person__name">DR COLIN MARSH</p>
      <p class="person__role">R&amp;D Engineer</p>
    </div>

    <div class="contact-icons" aria-hidden="true">
      <svg viewBox="0 0 24 24"><circle cx="12" cy="12" r="12" fill="#0b1f63"/><path d="M7 9.5c0-1 1-1.8 5-1.8s5 .8 5 1.8v1h-2.5v-1h-5v1H7z M8.5 11.5h7l1 4.5h-9z" fill="#fff"/></svg>
      <svg viewBox="0 0 24 24"><circle cx="12" cy="12" r="12" fill="#0b1f63"/><rect x="6.5" y="8" width="11" height="8" fill="#fff"/><path d="M6.5 8l5.5 4.5L17.5 8" fill="none" stroke="#0b1f63" stroke-width="1"/></svg>
      <svg viewBox="0 0 24 24"><circle cx="12" cy="12" r="12" fill="#0b1f63"/><circle cx="12" cy="12" r="5.5" fill="none" stroke="#fff" stroke-width="1.6"/><path d="M6.5 12h11M12 6.5c-2.5 3-2.5 8 0 11M12 6.5c2.5 3 2.5 8 0 11" fill="none" stroke="#fff" stroke-width="1"/></svg>
    </div>

    <div class="contacts">
      <p>0427 563 210</p>
      <p>colin@wombatdevicesco.com.au</p>
      <p>www.wombatdevicesco.com.au</p>
    </div>

    <div class="divider"></div>

    <div class="address">
      <p>PO Box XXX</p>
      <p>Banks ACT 2913, Australia</p>
    </div>
  </section>

  <section class="card card--back" aria-label="Business card back">
    <div class="back-mark">
      <div class="back-mark__dot"></div>
      <p class="back-mark__name">WOMBAT<br>DEVICES</p>
    </div>
    <ul class="services">
      <li>Applied electromagnetics</li>
      <li>RF and high speed electronics</li>
      <li>Signal and image processing</li>
      <li>Electro-optical and laser systems</li>
    </ul>
  </section>
</body>
</html>
```